July 2022 Industrial Manufacturer Product Expo Mexico City

We manufacture large screws and fastners for large Mining equipment, Trains, large ships, airplanes, wind turbines, and so on. We also do custom work base on the customer needs. No matter the size we can make it.
We have a Expo coming up with companies all over the world. We have to stand out we are a family own business so our customer service will be above and beyond anyone can provide. We do not have a sales force to push our products and services we provide one on one service.
Plus@!! I'm looking for anything that you designers can come up with if it was your company to put on a business card, plus i want to do a 1 or 2 sided pamphlet, and then a website. We make Speciality Bolts for large mining equipment these bolts can be 3 to 4 foot long!!! Plus fasteners, Nuts, washers, any, size, strengths, special materials, we offer more of a ono on one customer service, We are a small company, family own, but can fulfill any type of orders. We can also provide special time lines for emergency orders. "We keep the machines running we here at RWK don't believe in down time" We want to hear any slogan based on our company to stand out.
Thanks i really appreciate all your work and options that we have to pick on. Plus just a thought we could possibly want to entertain a experience Marketing internet help maybe a employment possibility. Thanks
Updates

I need 2 cards one in Spanish and English Like the steel back ground maybe send me in some bright red and blue writing Same with the Black cards Please remove the word Military The logo RWK maybe integrate a picture of a Bolt 🔩 Thank you

Still looking for I need 2 cards one in Spanish and English Like the steel back ground maybe send me in some bright red and blue writing Same with the Black cards try bright writing Please remove the word Military The logo RWK maybe integrate a picture of a Bolt 🔩 Plus will need the company to make a brochure and website next Thank you

Target Market(s)

Large Mining, Ship, Train, Green Energy, OPRE, and Government equipment. Throughout the World

Industry/Entity Type

We can Custom Manufacture any type of Fastners for Mining equipment, Trains, Ships, Green energy, Governments, or military projects. wind turbines,

Contact Information for Business Card

I attached the name and contact info that's on a card, plus the Company Logo. Would like industrial looking background with Bright Colors that will stand out!! If we can insert somewhere maybe on back that we "Custom Manufacture Any Size or Quantity Fastners for Large Mining Equipment, Trains, Ships, Green Energy Equipment or Government Projects

Font styles to use
Other font styles liked:
• You Pick, has to be bold, colorful standout, Professional looking Beable to read it.

Colors

Designer to choose colors to be used in the design.

Requirements
Must have
• Need in Spanish and English TO STANDOUT FROM THE REST OF THE EXPO!! See Business card details, Rounded corners
Nice to have
• Can i see some of the darker cards with Bright Red and Blue letters I like to see the different type of card material, heavy thickness, plastic, transparent, Metal types, Bright Colors, I saw like Raised letters like on the logo.

```html
<!DOCTYPE html>
<html lang="es">
<head>
<meta charset="utf-8">
<title>RWK – Tarjetas de presentación</title>
<link href="https://fonts.googleapis.com/css2?family=Michroma&family=Montserrat:wght@500;800&display=swap" rel="stylesheet">
<style>
  :root{
    --stage:#1d1d1e;
    --card-black:#0b0b0c;
    --card-steel:#2a2b2e;
    --silver:#c9cbd0;
    --silver-bright:#f2f3f5;
    --brand-blue:#2f8fe4;
    --navy:#232a7a;
    --panel-top:#3a3aa6;
    --panel-bottom:#2ba6ee;
    --white:#ffffff;
  }
  *{box-sizing:border-box;margin:0;padding:0}
  html,body{width:1200px;height:1200px;overflow:hidden;background:var(--stage)}
  .stage{position:relative;width:1200px;height:1200px;
    background:radial-gradient(ellipse at 50% 40%,#2a2a2c 0%,var(--stage) 70%)}
  .card{position:absolute;left:220px;width:760px;height:434px;border-radius:20px;overflow:hidden;
    background:
      repeating-linear-gradient(0deg,rgba(255,255,255,.018) 0 1px,transparent 1px 3px),
      linear-gradient(180deg,var(--card-steel) 0%,var(--card-black) 45%,var(--card-black) 100%);
    box-shadow:0 14px 30px rgba(0,0,0,.55)}
  .card--back{top:150px}
  .card--front{top:616px}

  /* back */
  .back-mark{position:absolute;left:0;right:0;top:108px;text-align:center;
    font-family:"Michroma",sans-serif;font-size:108px;letter-spacing:10px;color:var(--silver)}
  .back-statement{position:absolute;left:20px;right:20px;top:276px;text-align:center;
    font-family:"Montserrat",sans-serif;font-weight:800;font-size:15.5px;line-height:1.7;
    letter-spacing:.4px;color:var(--white);text-transform:uppercase}
  .back-statement__line{display:block;white-space:nowrap}

  /* front */
  .front-mark{position:absolute;left:60px;top:26px;
    font-family:"Michroma",sans-serif;font-size:108px;letter-spacing:10px;color:var(--brand-blue)}
  .front-tagline{position:absolute;left:30px;top:162px;
    font-family:"Michroma",sans-serif;font-size:17px;color:var(--brand-blue)}
  .name-band{position:absolute;left:0;top:232px;width:556px;height:46px;
    background:linear-gradient(90deg,#a9abb1 0%,var(--silver-bright) 35%,#b9bbc0 70%,var(--silver-bright) 100%);
    display:flex;align-items:center;padding-left:62px}
  .name-band__text{font-family:"Michroma",sans-serif;font-size:19px;color:var(--navy);letter-spacing:.5px}
  .contacts{position:absolute;left:54px;top:300px;list-style:none;
    font-family:"Montserrat",sans-serif;font-weight:500;font-size:22px;color:var(--white);letter-spacing:1px}
  .contacts li{display:flex;align-items:center;gap:14px;height:34px}
  .contacts svg{width:20px;height:20px;flex:none}
  .side-panel{position:absolute;right:0;top:0;width:204px;height:100%;
    background:
      repeating-linear-gradient(0deg,rgba(255,255,255,.03) 0 1px,transparent 1px 3px),
      linear-gradient(180deg,var(--panel-top) 0%,var(--panel-bottom) 100%)}
</style>
</head>
<body>
<main class="stage">

  <section class="card card--back" aria-label="Reverso de la tarjeta">
    <div class="back-mark">RWK</div>
    <p class="back-statement">
      <span class="back-statement__line">Custom manufacture any size or quantity fastners for large</span>
      <span class="back-statement__line">mining equipment, trains, ships, green energy equipment</span>
      <span class="back-statement__line">or government projects</span>
    </p>
  </section>

  <section class="card card--front" aria-label="Frente de la tarjeta">
    <div class="front-mark">RWK</div>
    <p class="front-tagline">Fabricación Y distribución de tornillos</p>

    <div class="name-band"><span class="name-band__text">Lic. Daniela Ortega Ruiz</span></div>

    <ul class="contacts">
      <li>
        <svg viewBox="0 0 24 24" aria-hidden="true"><path fill="#2f8fe4" d="M6.6 10.8a15 15 0 0 0 6.6 6.6l2.2-2.2c.3-.3.7-.4 1-.2 1.1.4 2.3.6 3.6.6.6 0 1 .4 1 1V20c0 .6-.4 1-1 1A17 17 0 0 1 3 4c0-.6.4-1 1-1h3.5c.6 0 1 .4 1 1 0 1.3.2 2.5.6 3.6.1.3 0 .7-.2 1z"/></svg>
        Oficina 871 5550142
      </li>
      <li>
        <svg viewBox="0 0 24 24" aria-hidden="true"><rect x="6" y="2" width="12" height="20" rx="2" fill="none" stroke="#2f8fe4" stroke-width="2.4"/><circle cx="12" cy="18" r="1.2" fill="#2f8fe4"/></svg>
        Movil 8715550198
      </li>
      <li>
        <svg viewBox="0 0 24 24" aria-hidden="true"><rect x="2" y="5" width="20" height="14" rx="1.5" fill="#2f8fe4"/><path d="M3 6l9 7 9-7" fill="none" stroke="#0b0b0c" stroke-width="1.6"/></svg>
        rwk.ventas@ejemplo.com
      </li>
    </ul>

    <div class="side-panel"></div>
  </section>

</main>
</body>
</html>
```